Recruitment Agency in Texas, needs a stand out header letter

Our colours are red and grey and can be found on our website
just my logo will be sufficient and address...

Target Market(s)

Engineering Manufacturing

Colors
0094D4
00A9DD
6FCCEA
C7EBF8
E9F6FB
EB3D1F
EC4F4E
F09395
F8D3D4
FCEDEE

Requirements
Must have
• use colors red and grey
Should not have
• Please use same colors and font as my logo. My website is kelbrantstaffing.net

```html
<!DOCTYPE html>
<html lang="en">
<head>
<meta charset="utf-8">
<title>KelbrantStaffing Letterhead</title>
<link rel="stylesheet" href="https://fonts.googleapis.com/css2?family=Roboto:wght@400;700&family=Saira+Semi+Condensed:wght@300;600&display=swap">
<style>
  :root {
    --brand-red: #d7141f;
    --brand-grey: #626268;
    --page: #ecebee;
    --backdrop: #d9d9db;
    --ink: #161616;
    --bar-text: #e4e4e8;
  }
  * { margin: 0; padding: 0; box-sizing: border-box; }
  html, body {
    width: 1200px; height: 1151px; overflow: hidden;
    background: var(--backdrop);
  }
  .letterhead {
    position: absolute; left: 212px; top: 20px;
    width: 776px; height: 1112px;
    background: var(--page);
    font-family: "Roboto", Arial, sans-serif;
    color: var(--ink);
    font-size: 16.2px; line-height: 20.25px;
  }
  .accent-bar {
    position: absolute; left: 0; top: 73px;
    width: 76px; height: 31px;
    background: var(--brand-red);
  }
  .brand-name {
    position: absolute; left: 91px; top: 64px;
    font-family: "Saira Semi Condensed", Arial, sans-serif;
    font-weight: 600; font-size: 44px; line-height: 48px;
    letter-spacing: -1.2px;
    color: var(--brand-red);
    white-space: nowrap;
  }
  .address-bar {
    position: absolute; left: 422px; top: 73px;
    width: 354px; height: 31px;
    background: var(--brand-grey);
    color: var(--bar-text);
    font-family: "Saira Semi Condensed", Arial, sans-serif;
    font-weight: 300; font-size: 15px; line-height: 31px;
    text-align: center; letter-spacing: 0.3px;
  }
  .block { position: absolute; left: 92px; white-space: nowrap; }
  .block span { display: block; }
  .date { top: 186px; }
  .recipient { top: 231px; }
  .salutation { top: 360px; }
  .body-main { top: 397px; }
  .body-closing { top: 780px; }
  .sign-off { top: 854px; }
  .signatory { top: 933px; }
  .signatory .name { font-weight: 700; }
  .footer-band {
    position: absolute; left: 0; bottom: 0;
    width: 100%; height: 25px;
    background: var(--brand-grey);
  }
</style>
</head>
<body>
  <article class="letterhead">
    <header>
      <div class="accent-bar"></div>
      <div class="brand-name">KelbrantStaffing</div>
      <div class="address-bar">48 Alder Park Avenue Houston</div>
    </header>

    <p class="block date">Date: 5-Aug-2021</p>

    <p class="block recipient">
      <span>To</span>
      <span>Daniel Harper</span>
      <span>Managing Director</span>
      <span>XYZ Services Ltd.</span>
    </p>

    <p class="block salutation">Dear Harper,</p>

    <div class="block body-main">
      <span>Lorem ipsum dolor sit amet, consectetuer adipiscing elit, sed diam nonummy nibh</span>
      <span>euismod tincidunt ut laoreet dolore magna aliquam erat volutpat. Ut wisi enim ad</span>
      <span>minim veniam, quis nostrud exerci tation ullamcorper suscipit lobortis nisl ut aliquip ex</span>
      <span>ea commodo consequat. Duis autem vel eum iriure dolor in hendrerit in vulputate velit</span>
      <span>esse molestie consequat, vel illum dolore eu feugiat nulla facilisis at vero eros et</span>
      <span>accumsan et iusto odio dignissim qui blandit praesent luptatum zzril delenit augue</span>
      <span>duis dolore te feugait nulla facilisi.</span>
      <span>Lorem ipsum dolor sit amet, cons ectetuer adipiscing elit, sed diam nonummy nibh</span>
      <span>euismod tincidunt ut laoreet dolore magna aliquam erat volutpat. Ut wisi enim ad</span>
      <span>minim veniam, quis nostrud exerci tation ullamcorper suscipit lobortis nisl ut aliquip ex</span>
      <span>ea commodo consequat.</span>
      <span>Lorem ipsum dolor sit amet, consectetuer adipiscing elit, sed diam nonummy nibh</span>
      <span>euismod tincidunt ut laoreet dolore magna aliquam erat volutpat. Ut wisi enim ad</span>
      <span>minim veniam, quis nostrud exerci tation ullamcorper suscipit lobortis nisl ut aliquip ex</span>
      <span>ea commodo consequat. Duis autem vel eum iriure dolor in hendrerit in vulputate velit</span>
      <span>esse molestie consequat, vel illum dolore eu feugiat nulla facilisis at vero eros et</span>
      <span>accumsan et iusto odio dignissim qui blandit praesent luptatum zzril delenit augue</span>
      <span>duis dolore te feugait nulla facilisi.</span>
    </div>

    <div class="block body-closing">
      <span>Lorem ipsum dolor sit amet, consectetuer adipiscing elit, sed diam nonummy nibh</span>
      <span>euismod tincidunt ut laoreet dolore magna aliquam erat volutpat.</span>
    </div>

    <p class="block sign-off">Sincerely Yours,</p>

    <p class="block signatory">
      <span class="name">Owen Marsh</span>
      <span class="role">Founder/CEO</span>
    </p>

    <footer class="footer-band"></footer>
  </article>
</body>
</html>
```